Business Card Design Project

We consult with hotels on setting rates and maximizing a revenue strategy

Industry/Entity Type

Business

Contact Information for Business Card

I am not sure what I want. Our company offers high level consulting to hotels around the country but we are also laid back. I would like something that is professional but also shows the laid back side

```html
<!DOCTYPE html>
<html lang="en">
<head>
<meta charset="utf-8">
<title>Harborline Business Card – Back</title>
<link href="https://fonts.googleapis.com/css2?family=Open+Sans:wght@300;400;700&display=swap" rel="stylesheet">
<style>
  :root {
    --stage: #4e5d6b;
    --card-green: #1f7d5f;
    --card-white: #ffffff;
    --swoosh-dark: #1e1712;
    --text-light: #ffffff;
    --brand-dark: #1e1712;
  }
  * { margin: 0; padding: 0; box-sizing: border-box; }
  html, body {
    width: 1000px;
    height: 1200px;
    overflow: hidden;
    background: var(--stage);
    font-family: "Open Sans", Arial, sans-serif;
  }
  .stage {
    position: relative;
    width: 1000px;
    height: 1200px;
  }
  .side-label {
    position: absolute;
    top: 258px;
    left: 0;
    width: 1040px;
    text-align: center;
    font-weight: 300;
    font-size: 54px;
    color: var(--text-light);
    letter-spacing: 1px;
  }
  .card {
    position: absolute;
    left: 241px;
    top: 384px;
    width: 590px;
    height: 335px;
    overflow: hidden;
  }
  .card-bg {
    position: absolute;
    inset: 0;
  }
  .brand {
    position: absolute;
    left: 40px;
    top: 72px;
    display: flex;
    align-items: center;
    gap: 10px;
  }
  .brand-mark {
    width: 34px;
    height: 34px;
    background: var(--card-green);
  }
  .brand-name {
    font-weight: 700;
    font-size: 22px;
    color: var(--brand-dark);
    letter-spacing: 0.5px;
  }
  .holder-name {
    position: absolute;
    left: 58px;
    top: 169px;
    font-weight: 700;
    font-size: 24px;
    color: var(--text-light);
  }
  .contact-line {
    position: absolute;
    left: 53px;
    font-size: 20px;
    color: var(--text-light);
    white-space: nowrap;
  }
  .contact-line span + span { margin-left: 18px; }
  .contact-line.first { top: 212px; }
  .contact-line.second { top: 246px; }
  .web-address {
    position: absolute;
    right: 20px;
    top: 294px;
    font-size: 15px;
    color: var(--text-light);
  }
</style>
</head>
<body>
<main class="stage">
  <h1 class="side-label">BACK</h1>

  <section class="card">
    <svg class="card-bg" width="590" height="335" viewBox="0 0 590 335" aria-hidden="true">
      <rect class="field-green" width="590" height="335" fill="var(--card-green)"/>
      <path class="swoosh" d="M590 2 C510 100 300 172 0 162 V135 C300 142 500 92 586 0 Z" fill="var(--swoosh-dark)"/>
      <path class="field-white" d="M0 0 H586 C500 92 300 142 0 135 Z" fill="var(--card-white)"/>
    </svg>

    <div class="brand">
      <div class="brand-mark"></div>
      <div class="brand-name">HARBORLINE</div>
    </div>

    <h2 class="holder-name">Dana Whitfield</h2>
    <p class="contact-line first"><span>Regional Revenue Manager</span><span>Office 503 555 0148</span></p>
    <p class="contact-line second"><span>Fax 503 555 0192</span><span>Dana@HarborlineRMS.com</span></p>
    <p class="web-address">www.HarborlineRMS.com</p>
  </section>
</main>
</body>
</html>
```